The name of my company is Tolland Refacing LLC and I would like the sub text to say "Cabinet Refacing and Countertops". Have my name Morris Pelton, Owner / Sales, contact info: Cell: 360-555-0147 / Email: morris.pelton@quillbox.net

Simple, Clean, and Organized. With colors that will appeal to the eye.

Target Market(s)

Houses and Apartments

Industry/Entity Type

Cabinet Refacing

Contact Information for Business Card

Company name and sub text Morris Pelton - Owner / Sales, my cell phone number and email

Requirements
Must have
• Business name, my name / position, and my contact info
Nice to have
• Simple. Organized. Appealing to the eye

```html
<!DOCTYPE html>
<html lang="en">
<head>
<meta charset="UTF-8">
<title>Tolland Refacing LLC — Business Card</title>
<link href="https://fonts.googleapis.com/css2?family=Montserrat:wght@400;500;700&display=swap" rel="stylesheet">
<style>
  :root {
    --page: #2a2b2f;
    --card: #121214;
    --edge: #4a72c4;
    --brand-blue: #4f76c6;
    --ink-light: #d9dbe0;
    --ink-soft: #b9bcc4;
  }
  * { box-sizing: border-box; margin: 0; padding: 0; }
  html, body {
    width: 1200px; height: 900px; overflow: hidden;
    background: var(--page);
    font-family: "Montserrat", Arial, sans-serif;
  }
  .stage {
    width: 1200px; height: 900px;
    display: flex; flex-direction: column; align-items: center; justify-content: center;
    gap: 48px;
  }
  .card {
    position: relative;
    width: 620px; height: 354px;
    background: var(--card);
    border-radius: 22px;
    border: 3px solid var(--edge);
  }
  .wordmark {
    display: flex; align-items: center; gap: 14px;
    color: var(--ink-light);
  }
  .wordmark__square {
    width: 22px; height: 22px; background: var(--brand-blue); flex: none;
  }
  .wordmark__name {
    font-weight: 400; letter-spacing: 0.06em; text-transform: uppercase;
  }
  .tagline {
    color: var(--ink-light); text-transform: uppercase;
    letter-spacing: 0.12em; font-weight: 500;
  }

  /* front */
  .card--front {
    display: flex; flex-direction: column; align-items: center; justify-content: center; gap: 14px;
  }
  .card--front .wordmark__name { font-size: 34px; }
  .card--front .tagline { font-size: 13px; }

  /* back */
  .card--back .brand {
    position: absolute; left: 44px; top: 52px;
    display: flex; flex-direction: column; gap: 10px;
  }
  .card--back .wordmark__square { width: 18px; height: 18px; }
  .card--back .wordmark__name { font-size: 26px; }
  .card--back .tagline { font-size: 10px; padding-left: 32px; }

  .person {
    position: absolute; left: 44px; top: 172px;
  }
  .person__name {
    color: var(--brand-blue); font-weight: 700; font-size: 26px; line-height: 1.1;
  }
  .person__role {
    color: var(--ink-light); font-size: 14px; margin-top: 4px;
  }
  .divider {
    position: absolute; left: 44px; right: 34px; top: 240px;
    height: 1.5px; background: var(--edge);
  }
  .contact {
    position: absolute; left: 44px; top: 258px;
    list-style: none; display: flex; flex-direction: column; gap: 9px;
  }
  .contact__item {
    display: flex; align-items: center; gap: 12px;
    color: var(--ink-light); font-size: 15px;
  }
  .contact__icon { width: 14px; height: 14px; fill: var(--brand-blue); flex: none; }
</style>
</head>
<body>
<main class="stage">
  <section class="card card--front" aria-label="Card front">
    <div class="wordmark">
      <span class="wordmark__square"></span>
      <span class="wordmark__name">Tolland Refacing, LLC</span>
    </div>
    <p class="tagline">Cabinet Refacing and Countertops</p>
  </section>

  <section class="card card--back" aria-label="Card back">
    <div class="brand">
      <div class="wordmark">
        <span class="wordmark__square"></span>
        <span class="wordmark__name">Tolland Refacing, LLC</span>
      </div>
      <p class="tagline">Cabinet Refacing and Countertops</p>
    </div>

    <div class="person">
      <p class="person__name">Morris Pelton</p>
      <p class="person__role">Owner / Sales</p>
    </div>

    <div class="divider"></div>

    <ul class="contact">
      <li class="contact__item">
        <svg class="contact__icon" viewBox="0 0 24 24" aria-hidden="true"><path d="M6.6 10.8a15.2 15.2 0 0 0 6.6 6.6l2.2-2.2a1 1 0 0 1 1-.25 11.4 11.4 0 0 0 3.6.6 1 1 0 0 1 1 1V20a1 1 0 0 1-1 1A17 17 0 0 1 3 4a1 1 0 0 1 1-1h3.5a1 1 0 0 1 1 1c0 1.25.2 2.45.6 3.6a1 1 0 0 1-.25 1z"/></svg>
        <span>360-555-0147</span>
      </li>
      <li class="contact__item">
        <svg class="contact__icon" viewBox="0 0 24 24" aria-hidden="true"><path d="M2 5h20v14H2z M2 5l10 8 10-8" /></svg>
        <span>morris.pelton@quillbox.net</span>
      </li>
    </ul>
  </section>
</main>
</body>
</html>
```